Local Horticulturalist needs Business card design

Meridale Gardening would like to update our existing business card and utilize our new logo (design attached)....we specialize in getting the best out of our customers yard with professional maintenance programs, expert pruning and hedging and garden restorations.
Utilizing colors from attached logo I would like a design that implies professionalism and if possible our businesses love of restoration through plants.
I also sometimes write down for my customers a start date and price on the back of my current card
Target Market(s)
Home owners
Contractors
Industry/Entity Type
Gardener
Contact Information for Business Card
Trevor Kalbrook | Horticulturalist
ph: 0452739186
meridalegard@fernpost.com
www.meridalegardening.com.au
Requirements
Must have
- crucial information easy to read
- incorporate current logo
- Horticulturalist listed preferably near name
Nice to have
- currently I write a job start date and price on the back of my current card so something that integrates this would be beneficial
Should not have
- be pretty or flowerey
- be too white or basic

```html
<!DOCTYPE html>
<html lang="en">
<head>
<meta charset="utf-8">
<title>Meridale Gardening – Business Card</title>
<link rel="stylesheet" href="https://fonts.googleapis.com/css2?family=Kurale&display=swap">
<style>
  :root {
    --stage: #eef7d2;
    --stage-light: #fbfff0;
    --bark: #857459;
    --bark-dark: #6f604a;
    --leaf: #8cc21f;
    --rule: #a3ad6c;
    --card-light: #fbfef2;
    --card-tint: #e7f6bf;
    --white: #ffffff;
  }
  * { margin: 0; padding: 0; box-sizing: border-box; }
  html, body {
    width: 1200px; height: 1000px; overflow: hidden;
  }
  body {
    position: relative;
    background: radial-gradient(ellipse at 55% 45%, var(--stage-light) 0%, var(--stage) 75%);
    font-family: "Kurale", Georgia, serif;
    color: var(--bark);
  }
  .card {
    position: absolute;
    width: 685px; height: 366px;
    background: linear-gradient(155deg, var(--card-tint) 0%, var(--card-light) 35%, var(--card-light) 60%, var(--card-tint) 100%);
    box-shadow: 0 6px 18px rgba(120, 130, 80, 0.25);
    overflow: hidden;
  }
  .card--front { left: 106px; top: 108px; }
  .card--back { left: 432px; top: 560px; }

  .band { position: absolute; left: 0; width: 100%; background: var(--bark); }
  .band--top { top: 0; height: 36px; }
  .band--contact {
    bottom: 0; height: 40px;
    display: flex; align-items: center; justify-content: center;
    color: var(--white); font-size: 20px; white-space: nowrap;
  }
  .contact-sep {
    display: inline-block; width: 1px; height: 26px;
    background: var(--white); margin: 0 6px;
  }

  .brand { position: absolute; display: flex; align-items: center; }
  .brand-mark { border-radius: 50%; background: var(--leaf); flex: none; }
  .brand-name { color: var(--bark-dark); line-height: 1; white-space: nowrap; }
  .brand-tagline {
    position: absolute; color: var(--bark); white-space: nowrap; letter-spacing: 0.06em;
  }

  .card--front .brand { left: 72px; top: 70px; }
  .card--front .brand-mark { width: 84px; height: 84px; margin-right: 14px; }
  .card--front .brand-name { font-size: 42px; }
  .card--front .brand-tagline { left: 170px; top: 128px; font-size: 17px; }
  .front-rule {
    position: absolute; left: 60px; top: 158px; width: 572px; height: 2px; background: var(--rule);
  }

  .person { position: absolute; left: 212px; top: 206px; width: 282px; text-align: center; }
  .person-name {
    font-size: 27px; line-height: 1.1; padding-bottom: 4px;
    border-bottom: 2px solid var(--bark);
  }
  .person-title { font-size: 18px; margin-top: 3px; }

  .card--back .brand { left: 172px; top: 40px; }
  .card--back .brand-mark { width: 52px; height: 52px; margin-right: 8px; }
  .card--back .brand-name { font-size: 26px; }
  .card--back .brand-tagline { left: 234px; top: 80px; font-size: 12px; }

  .services {
    position: absolute; left: 0; top: 128px; width: 100%; height: 134px;
    background: var(--bark); color: var(--white);
    list-style: none; text-align: center;
    font-size: 19px; line-height: 25.5px; padding-top: 3px;
  }

  .job-notes { position: absolute; left: 200px; top: 288px; width: 143px; text-align: right; font-size: 19px; line-height: 23px; }
</style>
</head>
<body>

  <section class="card card--front" aria-label="Business card front">
    <div class="band band--top"></div>
    <div class="brand">
      <span class="brand-mark"></span>
      <span class="brand-name">Meridale Gardening</span>
    </div>
    <p class="brand-tagline">Garden Restorations &amp; Maintenance</p>
    <div class="front-rule"></div>
    <div class="person">
      <p class="person-name">Trevor Kalbrook</p>
      <p class="person-title">Horticulturalist</p>
    </div>
    <div class="band band--contact">
      <span>045-273-9186</span><span class="contact-sep"></span>
      <span>meridalegard@fernpost.com</span><span class="contact-sep"></span>
      <span>meridalegardening.com.au</span>
    </div>
  </section>

  <section class="card card--back" aria-label="Business card back">
    <div class="brand">
      <span class="brand-mark"></span>
      <span class="brand-name">Meridale Gardening</span>
    </div>
    <p class="brand-tagline">Garden Restorations &amp; Maintenance</p>
    <ul class="services">
      <li>Restore your garden to its former glory</li>
      <li>Design and cultivate your new garden or landscape</li>
      <li>Make your garden more water friendly with drip irrigation</li>
      <li>Keep your indoor plants alive and thriving</li>
      <li>Grow a productive home fruit and vegie garden</li>
    </ul>
    <div class="job-notes">
      <p>Start Date:</p>
      <p>Price:</p>
    </div>
  </section>

</body>
</html>
```